Maple Lantern Senior Care

Just had our logo redesigned and want to get all supporting collateral, business cards, postcards, brochure, etc to go together, but the business cards are the current priority.
We are an agency who provides care for seniors to help them with activities of daily living and companionship in their own home. I have attached our color guidelines and our logo, as well as a copy of our current card for your reference. Our clients are seniors 65+ We would like to see something somewhat conservative but creative (we are getting rid of the desert background), double sided full color (back should have our mission statement and services as it does in the current one) Thanks a million for looking! I am looking forward to seeing what you come up with!
Target Market(s)
65+ baby boomers and 80+ Seniors
Industry/Entity Type
Conservative
Look and feel
Each slider illustrates characteristics of the customer's brand and the style your logo design should communicate.

```html
<!DOCTYPE html>
<html lang="en">
<head>
<meta charset="utf-8">
<title>Maple Lantern Senior Care – Business Card</title>
<link rel="stylesheet" href="https://fonts.googleapis.com/css2?family=Carlito:wght@400;700&display=swap">
<style>
  :root {
    --navy: #0f3d6b;
    --blue: #14659b;
    --green: #8cc63f;
    --green-light: #a6d85c;
    --ink: #2b2b2b;
    --grey: #5a5a5a;
    --paper: #ffffff;
    --backdrop: #e7e7e5;
  }
  * { margin: 0; padding: 0; box-sizing: border-box; }
  html, body { width: 1200px; height: 800px; overflow: hidden; }
  body {
    background: var(--backdrop);
    font-family: "Carlito", "Calibri", sans-serif;
    position: relative;
  }
  .card {
    position: absolute;
    top: 245px;
    width: 540px;
    height: 309px;
    background: var(--paper);
    overflow: hidden;
    box-shadow: 0 6px 18px rgba(0,0,0,0.18);
  }
  .card svg.art { position: absolute; inset: 0; }

  /* Back side */
  .card--back { left: 40px; }
  .badge-column {
    position: absolute; left: 18px; top: 34px;
    display: flex; flex-direction: column; gap: 16px;
  }
  .badge { width: 64px; height: 48px; background: #d6dde6; border-radius: 4px; }
  .badge--round { border-radius: 50%; width: 52px; margin-left: 6px; }
  .tagline {
    position: absolute; left: 150px; top: 26px;
    color: var(--blue); font-weight: 700; font-size: 18px; letter-spacing: 0.6px;
  }
  .service-list {
    position: absolute; top: 62px; list-style: none;
    color: var(--ink); font-size: 15px; line-height: 25px;
  }
  .service-list--one { left: 150px; }
  .service-list--two { left: 340px; }
  .service-list li::before {
    content: ""; display: inline-block; width: 7px; height: 7px;
    border-radius: 50%; background: var(--blue); margin-right: 8px; vertical-align: 2px;
  }

  /* Front side */
  .card--front { left: 620px; }
  .contact {
    position: absolute; left: 24px; top: 30px; list-style: none;
    color: var(--grey); font-size: 14px; line-height: 22px;
  }
  .contact .line { display: flex; align-items: center; gap: 8px; }
  .contact .icon {
    width: 13px; height: 13px; border-radius: 50%; background: var(--blue);
    display: inline-flex; align-items: center; justify-content: center;
  }
  .contact .address { margin-top: 8px; }
  .brand {
    position: absolute; left: 258px; top: 72px; width: 240px;
    display: flex; align-items: center; gap: 8px;
    color: var(--navy); font-weight: 700; font-size: 24px; line-height: 1.05;
  }
  .brand .mark { width: 16px; height: 16px; border-radius: 50%; background: var(--green); flex: none; }
  .person {
    position: absolute; left: 300px; top: 158px;
  }
  .person .name { color: var(--navy); font-weight: 700; font-size: 20px; letter-spacing: 0.5px; }
  .person .role { color: var(--ink); font-size: 14px; margin-top: 2px; }
</style>
</head>
<body>

<section class="card card--back" aria-label="Card back: mission and services">
  <svg class="art" width="540" height="309" viewBox="0 0 540 309" aria-hidden="true">
    <path d="M120 0 C95 60 80 110 105 160 C130 210 120 260 140 309 L540 309 L540 0 Z" fill="var(--green)"/>
    <path d="M60 0 C120 10 125 40 120 0" fill="none"/>
    <path d="M85 0 C115 18 122 40 118 60" stroke="var(--blue)" stroke-width="5" fill="none"/>
    <path d="M128 240 C132 275 150 300 190 309" stroke="var(--blue)" stroke-width="5" fill="none"/>
    <circle cx="330" cy="170" r="80" fill="var(--green-light)" opacity="0.35"/>
  </svg>
  <div class="badge-column" aria-label="Partner memberships">
    <div class="badge"></div>
    <div class="badge badge--round"></div>
    <div class="badge"></div>
    <div class="badge"></div>
  </div>
  <h2 class="tagline">COMPASSION, DIGNITY, DEPENDABILITY...</h2>
  <ul class="service-list service-list--one">
    <li>Companionship</li>
    <li>Errands and Doctor’s visits</li>
    <li>Personal Care</li>
    <li>Medication Management</li>
    <li>Advocacy</li>
  </ul>
  <ul class="service-list service-list--two">
    <li>Light Housekeeping</li>
    <li>Meal Preparation</li>
    <li>Assisted Living Placement</li>
    <li>Dementia and Alzheimer’s Care</li>
    <li>Bonded and Insured</li>
  </ul>
</section>

<section class="card card--front" aria-label="Card front: contact details">
  <svg class="art" width="540" height="309" viewBox="0 0 540 309" aria-hidden="true">
    <circle cx="420" cy="160" r="190" fill="var(--blue)"/>
    <circle cx="442" cy="152" r="170" fill="var(--paper)"/>
    <circle cx="442" cy="152" r="164" fill="var(--green)"/>
    <circle cx="450" cy="148" r="154" fill="var(--paper)"/>
  </svg>
  <ul class="contact">
    <li class="line"><span class="icon"><svg width="7" height="7" viewBox="0 0 10 10"><path d="M2 1 L4 1 L5 3 L4 4 Q5 6 6 6 L7 5 L9 6 L9 8 Q5 9 2 5 Q1 3 2 1Z" fill="#fff"/></svg></span>555-204-3318</li>
    <li class="line"><span class="icon"><svg width="7" height="7" viewBox="0 0 10 10"><rect x="1" y="3" width="8" height="6" fill="#fff"/><rect x="3" y="1" width="4" height="3" fill="#fff"/></svg></span>555-671-0942</li>
    <li class="line"><span class="icon"><svg width="7" height="7" viewBox="0 0 10 10"><rect x="1" y="2" width="8" height="6" fill="#fff"/><path d="M1 2 L5 6 L9 2" stroke="var(--blue)" fill="none"/></svg></span>helen@maplelanterncare.com</li>
    <li class="address">88 Orchard Bend Lane</li>
    <li>Fairview AZ 85000</li>
    <li>www.MapleLanternCare.com</li>
  </ul>
  <div class="brand"><span class="mark"></span><span>Maple Lantern Senior Care</span></div>
  <div class="person">
    <div class="name">HELEN MARSH</div>
    <div class="role">CEO | Executive Director</div>
  </div>
</section>

</body>
</html>
```